Poster Design for company teaching children how to cook

Bright Pantry is a local business providing 2 key services (and 1 lesser):
1. After School Cookery clubs
2. Parties
(3. Cookery Classes for pre-schoolers)
A good summary can be found at our website www.bright-pantry.co.uk
We want a poster that we can display at various events, for example, outside parties, alongside demonstrations and in schools. We also would like to replicate the design for advertisement use in press.
We want to communicate that our classes and parties are good fun whilst at the same time being great for children's confidence and skills.
Please contact me tom@bright-pantry.co.uk with any questions and for company logo files.

Now I have sorted out the wording as follows, thanks for your patience:

inspiring children to cook (n.b. lower case as is the wording in the logo)

Classes

- Create nutritious food from scratch that can be replicated at home

- Increase confidence and skills in the kitchen

- Promote awareness of the importance of a nutritionally balanced diet

Parties

- Let us take the stress and run the party for you by providing the entertainment at the same time as the catering

- A variety of sweet and savoury dishes to choose from

- Party bags and invitations included

Call Morwenna now on 07519 620387 for more information or visit www.bright-pantry.co.uk

Since the call to action now contains contact details these need not be repeated elsewhere

Target Market(s)

Children at our classes are generally in the primary school age group 6-11 year olds although our parties reach a slightly wider group 4-13.
We obviously look to appeal to this group directly but also appealing to their parents, the budget holders, should not be underestimated!

Requirements
Must have
• A strong image (please pick from attachments)
• Company logo
• Company contact details including website, email address and phone
• Strapline / Call to action (Wording to be confirmed)
• Two textual areas where we can describe the benefits from parties/classes (about 40-50 words maximum in each. Wording to be confirmed)
• Any use of colour needs to be consistent with the logo palette
• colours are CMYK - Navy & Caribbean Blue
• green - CMYK Mint Julep
• purple - CMYK Amethyst
• Blue - CMYK Caribbean Blue
• Purple light
• C 0
• M 100
• Y 0
• K 0
• Purple dark
• C 50
• M 100
• Y 0
• K 0
• Green light
• C 50
• M 0
• Y 100
• K 0
• Green dark
• C 75
• M 0
• Y 100
• K 25
• Blue light
• C 100
• M 0
• Y 0
• K 0
• Blue dark
• C 100
• M 50
• Y 0
• K 0
• Font in Logo is "Brasserie". Any other font used should be unfussy and clear.
Nice to have
• Subject to space and design, maybe a testimonial or two (Wording to be confirmed)
Should not have
• The image should dominate, not the company logo
• No cartoony illustrations

```html
<!DOCTYPE html>
<html lang="en">
<head>
<meta charset="utf-8">
<title>Bright Pantry – inspiring children to cook</title>
<link rel="stylesheet" href="https://fonts.googleapis.com/css2?family=Arimo:wght@400;700&family=Noto+Serif:wght@700&display=swap">
<style>
  :root {
    --green: #8cc63f;
    --green-dark: #3f9a2c;
    --green-pale: #eef7c8;
    --navy: #173a66;
    --white: #ffffff;
    --purple: #7b2d8e;
    --blue: #00a3e0;
  }
  html, body {
    margin: 0;
    padding: 0;
    overflow: hidden;
    background: #ffffff;
  }
  .poster {
    position: relative;
    width: 850px;
    height: 1200px;
    overflow: hidden;
    background: var(--green);
    font-family: "Arimo", Arial, sans-serif;
    color: var(--white);
  }
  .hero-photo {
    position: absolute;
    left: 0;
    top: 0;
    width: 850px;
    height: 557px;
    background:
      radial-gradient(ellipse at 45% 40%, #e9c6a8 0%, #c89a7a 30%, transparent 60%),
      radial-gradient(ellipse at 40% 35%, #d23a3a 0%, transparent 25%),
      linear-gradient(180deg, #b98f63 0%, #8a6a4c 45%, #6f86a8 100%);
  }
  .brand-band {
    position: absolute;
    left: 0;
    top: 490px;
    width: 850px;
    height: 110px;
  }
  .brand-name {
    position: absolute;
    left: 20px;
    top: 526px;
    display: flex;
    align-items: center;
    gap: 8px;
    font-family: "Arimo", Arial, sans-serif;
    font-weight: 700;
    font-size: 22px;
    color: var(--purple);
  }
  .brand-dot {
    width: 14px;
    height: 14px;
    border-radius: 50%;
    background: var(--blue);
  }
  .strapline {
    position: absolute;
    left: 396px;
    top: 548px;
    margin: 0;
    font-family: "Noto Serif", Georgia, serif;
    font-weight: 700;
    font-size: 29px;
    letter-spacing: -0.3px;
    color: var(--white);
  }
  .party-photo {
    position: absolute;
    left: 29px;
    top: 612px;
    width: 278px;
    height: 312px;
    background:
      radial-gradient(ellipse at 30% 60%, #e8c9b0 0%, transparent 45%),
      linear-gradient(160deg, #c9a98c 0%, #a8624c 50%, #6b4a3a 100%);
  }
  .testimonial {
    position: absolute;
    left: 29px;
    top: 930px;
    width: 278px;
    height: 130px;
    margin: 0;
    padding: 10px 8px;
    box-sizing: border-box;
    font-size: 17px;
    line-height: 21px;
    color: var(--green-pale);
    text-align: justify;
  }
  .testimonial cite {
    display: block;
    font-style: normal;
    padding-left: 34px;
    text-align: left;
  }
  .services {
    position: absolute;
    left: 324px;
    top: 628px;
    width: 480px;
  }
  .service-title {
    margin: 0 0 14px;
    font-family: "Noto Serif", Georgia, serif;
    font-weight: 700;
    font-size: 21px;
    color: var(--white);
  }
  .service-list {
    list-style: none;
    margin: 0 0 36px;
    padding: 0;
  }
  .service-list li {
    position: relative;
    padding-left: 16px;
    margin-bottom: 24px;
    font-size: 16.5px;
    line-height: 22px;
  }
  .service-list li::before {
    content: "-";
    position: absolute;
    left: 0;
  }
  .call-bar {
    position: absolute;
    left: 0;
    top: 1142px;
    width: 850px;
    height: 58px;
    background: var(--navy);
    display: flex;
    align-items: center;
    justify-content: center;
    font-size: 20px;
    font-weight: 700;
    color: var(--green);
  }
  .call-bar strong {
    color: var(--white);
  }
</style>
</head>
<body>
<main class="poster">
  <div class="hero-photo" role="img" aria-label="Photo of a young boy in a chef's hat holding up a fruit skewer of strawberries and banana"></div>

  <svg class="brand-band" viewBox="0 490 850 110" width="850" height="110" aria-hidden="true">
    <path d="M0 500 Q75 495 150 512 Q168 525 176 540 L708 548 L176 556 Q168 572 150 585 Q75 596 0 592 Z" fill="#ffffff"/>
  </svg>

  <div class="brand-name"><span class="brand-dot"></span>Bright Pantry</div>

  <h1 class="strapline">inspiring children to cook</h1>

  <div class="party-photo" role="img" aria-label="Photo of a small child in a chef's hat enjoying a cookery party"></div>

  <blockquote class="testimonial">
    “All of the kids were having fun and the best part is it's the most worry free party we ever had for Elsie.”
    <cite>- Simon &amp; Kate Harding</cite>
  </blockquote>

  <section class="services">
    <h2 class="service-title">Classes</h2>
    <ul class="service-list">
      <li>Create nutritious food from scratch that can be replicated at home</li>
      <li>Increase confidence and skills in the kitchen</li>
      <li>Promote awareness of the importance of a nutritionally balanced diet</li>
    </ul>

    <h2 class="service-title">Parties</h2>
    <ul class="service-list">
      <li>Let us take the stress and run the party for you by providing the entertainment at the same time as the catering</li>
      <li>A variety of sweet and savoury dishes to choose from</li>
      <li>Party bags and invitations included</li>
    </ul>
  </section>

  <footer class="call-bar">
    <span>Call Morwenna now on 07519 620387 for more information or visit&nbsp;<strong>www.bright-pantry.co.uk</strong></span>
  </footer>
</main>
</body>
</html>
```